Tamarack Hearth Partners Business Card

Looking for a new business card layout. We are a real estate firm w/ a logo, old design attached. Must keep the same elements on there, just need a fresh look and possible some foil accents. Looking for a simpler design w/ more modern style.

Target Market(s)

Real Estate clients

Industry/Entity Type

Real Estate Agent

Contact Information for Business Card

see attached

Font styles to use
Sans Serif

Requirements
Must have
• all elements on current biz card
Nice to have
• modern look, simpler than we have!
Should not have
• no serif fonts

```html
<!DOCTYPE html>
<html lang="en">
<head>
<meta charset="utf-8">
<title>Tamarack Hearth Partners Business Card</title>
<link rel="stylesheet" href="https://fonts.googleapis.com/css2?family=Poppins:wght@400;500;600&display=swap">
<style>
  :root {
    --page: #e6e6e6;
    --card-grey: #8f8f8f;
    --mark-grey: #5e5e5e;
    --panel-black: #050505;
    --text-white: #ffffff;
    --mark-light: #bdbdbd;
    --bar-grey: #9a9a9a;
    --bar-text: #111111;
    --photo-light: #e9e1d6;
    --photo-mid: #d6bf9c;
    --photo-teal: #3fbfbf;
  }
  * { box-sizing: border-box; margin: 0; padding: 0; }
  html, body { width: 1200px; height: 874px; overflow: hidden; }
  body {
    background: var(--page);
    font-family: "Poppins", sans-serif;
    position: relative;
  }
  .card {
    position: absolute;
    left: 250px;
    width: 700px;
    height: 400px;
    border-radius: 22px;
    overflow: hidden;
    box-shadow: 0 6px 18px rgba(0,0,0,0.18);
  }
  .card-back { top: 20px; background: var(--card-grey); display: flex; align-items: center; justify-content: center; }
  .card-front { top: 454px; background: var(--panel-black); }

  .brand-name {
    font-weight: 600;
    text-transform: uppercase;
    line-height: 1.05;
    text-align: center;
  }
  .card-back .brand-name { color: var(--mark-grey); font-size: 50px; letter-spacing: 1px; }

  .portrait {
    position: absolute; left: 0; top: 0; width: 330px; height: 400px;
    background: linear-gradient(170deg, var(--photo-light) 0%, var(--photo-mid) 55%, var(--photo-teal) 100%);
  }
  .details {
    position: absolute; right: 44px; top: 34px; width: 320px;
    text-align: right; color: var(--text-white);
  }
  .card-front .brand-name { color: var(--mark-light); font-size: 30px; text-align: right; margin-bottom: 22px; }
  .agent-name { font-size: 22px; font-weight: 600; letter-spacing: 0.5px; line-height: 1.1; }
  .agent-title { font-size: 14px; font-weight: 500; letter-spacing: 0.5px; margin-bottom: 18px; }
  .address { font-size: 15px; line-height: 1.35; margin-bottom: 12px; }
  .contact-line { font-size: 15px; line-height: 1.4; display: flex; justify-content: flex-end; align-items: center; gap: 8px; }
  .contact-line svg { width: 14px; height: 14px; fill: none; stroke: var(--text-white); stroke-width: 1.8; }
  .web-bar {
    position: absolute; left: 290px; right: 0; bottom: 26px; height: 36px;
    background: var(--bar-grey); color: var(--bar-text);
    font-size: 15px; font-weight: 500; display: flex; align-items: center; padding-left: 40px;
  }
</style>
</head>
<body>
  <section class="card card-back">
    <p class="brand-name">Tamarack Hearth<br>Partners</p>
  </section>

  <section class="card card-front">
    <div class="portrait" role="img" aria-label="Portrait photo of the principal broker"></div>
    <div class="details">
      <p class="brand-name">Tamarack Hearth<br>Partners</p>
      <p class="agent-name">MARISA LUND</p>
      <p class="agent-title">PRINCIPAL BROKER</p>
      <p class="address">318 NE Alder Ln<br>Sisters Creek, OR 97759</p>
      <p class="contact-line">555.210.4830
        <svg viewBox="0 0 16 16"><path d="M4 2l2.5 3-1.5 1.5c1 2 2.5 3.5 4.5 4.5L11 9.5 14 12l-1.5 2C7 14 2 9 2 3.5z"/></svg>
      </p>
      <p class="contact-line">555.318.2264
        <svg viewBox="0 0 16 16"><rect x="4.5" y="1.5" width="7" height="13" rx="1.2"/><path d="M7 12.5h2"/></svg>
      </p>
      <p class="contact-line">marisa@tamarackhearth.com
        <svg viewBox="0 0 16 16"><rect x="1.5" y="3.5" width="13" height="9"/><path d="M1.5 3.5L8 9l6.5-5.5"/></svg>
      </p>
    </div>
    <div class="web-bar">www.TamarackHearth-Homes.com</div>
  </section>
</body>
</html>
```